Looking for a Lumora Book Cover

My book has been online for a while and I am now looking for a professional cover for it as it has been very well received.

You can view the book here and all the details about it:

https://www.pagevaultshop.example/dp/X7Q2KRMTPL#readerNotes

Not sure what I am looking for as a design, just open to your ideas.

I want something different that will stand out please.

Thanks
Owen

```html
<!DOCTYPE html>
<html lang="en">
<head>
<meta charset="utf-8">
<title>Roots and Resilience – Book Cover</title>
<link href="https://fonts.googleapis.com/css2?family=Cinzel:wght@400;500&family=Montserrat:wght@400;500&display=swap" rel="stylesheet">
<style>
  :root {
    --page: #ffffff;
    --cover-black: #000000;
    --gold: #c1994a;
    --teal: #4f7c7a;
    --red: #c8462f;
    --orange: #f39325;
    --ink: #1a1a1a;
    --white: #ffffff;
    --tan: #cdb68f;
  }
  * { margin: 0; padding: 0; box-sizing: border-box; }
  html, body {
    width: 1200px; height: 1200px; overflow: hidden;
    background: var(--page);
  }
  .cover {
    position: absolute; left: 222px; top: 34px;
    width: 762px; height: 1143px;
    background: var(--cover-black);
    overflow: hidden;
  }
  .title-roots {
    position: absolute; top: 30px; left: 0; width: 100%;
    text-align: center;
    font-family: "Cinzel", serif; font-weight: 400;
    font-size: 168px; line-height: 1; letter-spacing: -3px;
    color: var(--gold);
  }
  .title-and {
    position: absolute; top: 190px; left: 60px; right: 60px;
    display: flex; align-items: center; gap: 14px;
    font-family: "Cinzel", serif; font-size: 38px; line-height: 1;
    color: var(--teal);
  }
  .title-and::before, .title-and::after {
    content: ""; flex: 1; height: 3px; background: var(--teal);
  }
  .title-resilience {
    position: absolute; top: 228px; left: 0; width: 100%;
    text-align: center;
    font-family: "Cinzel", serif; font-weight: 400;
    font-size: 104px; line-height: 1; letter-spacing: -1px;
    color: var(--red);
  }
  .artwork {
    position: absolute; left: 0; top: 390px;
    width: 100%; height: 631px;
    background: linear-gradient(90deg,
      var(--red) 0%, #8a4a33 18%, var(--tan) 38%,
      #e9e1d2 50%, var(--gold) 64%, #7d7a58 80%, var(--teal) 100%);
  }
  .tagline-shadow {
    position: absolute; left: 97px; top: 376px;
    width: 555px; height: 85px; background: var(--white);
  }
  .tagline {
    position: absolute; left: 104px; top: 364px;
    width: 555px; height: 85px; background: var(--orange);
    display: flex; align-items: center; justify-content: center;
    text-align: center;
    font-family: "Montserrat", sans-serif; font-weight: 500;
    font-size: 26px; line-height: 1.25; letter-spacing: 1.5px;
    text-transform: uppercase; color: var(--ink);
  }
  .subtitle {
    position: absolute; left: 110px; top: 998px;
    width: 542px; height: 69px; background: var(--cover-black);
    display: flex; align-items: center; justify-content: center;
    text-align: center;
    font-family: "Montserrat", sans-serif; font-weight: 400;
    font-size: 22px; line-height: 1.15; color: var(--white);
  }
  .author {
    position: absolute; top: 1084px; left: 0; width: 100%;
    text-align: center;
    font-family: "Montserrat", sans-serif; font-weight: 400;
    font-size: 31px; letter-spacing: 2px; line-height: 1;
    text-transform: uppercase; color: var(--gold);
  }
</style>
</head>
<body>
  <main class="cover">
    <h1>
      <span class="title-roots">Roots</span>
      <span class="title-and">And</span>
      <span class="title-resilience">Resilience</span>
    </h1>
    <div class="artwork" role="img" aria-label="Word-art portrait of a woman with a large afro, formed from words like strong, proud, blessed, smart and justice in red, tan, gold and teal"></div>
    <div class="tagline-shadow"></div>
    <p class="tagline">A Celebration of Culture,<br>Struggle and Achievement</p>
    <p class="subtitle">The History, Resistance and Excellence of<br>Black People in Africa and the Diaspora</p>
    <p class="author">Desmond Harlow</p>
  </main>
</body>
</html>
```